Bright Harbor Theatre Academy Business Card

We need a professional looking card for the Bright Harbor Theatre Academy. The logo is attached.
The owner is: Marla Quintrell
Phone Number: 303-555-0147
Email: bhtheatreacademy@mailbox-example.com
Website: bhtheatre-example.com
Somewhere on the front of the card we would like to see the slogan: Step into the limelight
On the back we would like to see the quote: All the world's a stage. -Edmund Larkwood
We are open to different colors for the wording or maybe just black. Something that will go well with the logo.
Individuals seeking a professional children's theatre.
Business

```html
<!DOCTYPE html>
<html lang="en">
<head>
<meta charset="utf-8">
<title>Bright Harbor Theatre Academy – Business Card</title>
<link rel="stylesheet" href="https://fonts.googleapis.com/css2?family=Arimo&family=Yellowtail&display=swap">
<style>
  :root {
    --page: #ffffff;
    --frame: #000000;
    --card-black: #000000;
    --band-white: #ffffff;
    --curtain-red: #6b0c0c;
    --text-white: #ffffff;
    --text-black: #111111;
  }
  * { box-sizing: border-box; margin: 0; padding: 0; }
  html, body {
    width: 1200px;
    height: 900px;
    overflow: hidden;
    background: var(--page);
  }
  .canvas {
    position: relative;
    width: 1200px;
    height: 900px;
    border: 2px solid var(--frame);
    background: var(--page);
  }
  .card {
    position: absolute;
    left: 73px;
    top: 139px;
    width: 1058px;
    height: 590px;
    background: var(--card-black);
    font-family: "Arimo", Arial, sans-serif;
    color: var(--text-white);
  }
  .brand-band {
    position: absolute;
    left: 0;
    top: 145px;
    width: 100%;
    height: 113px;
    background: var(--band-white);
    display: flex;
    align-items: center;
    justify-content: center;
  }
  .brand-name {
    font-family: "Arimo", Arial, sans-serif;
    font-size: 40px;
    color: var(--text-black);
    letter-spacing: 0.5px;
  }
  .slogan {
    position: absolute;
    left: 0;
    top: 286px;
    width: 100%;
    text-align: center;
    font-family: "Yellowtail", cursive;
    font-size: 58px;
    line-height: 1;
    color: var(--text-white);
  }
  .owner {
    position: absolute;
    left: 0;
    top: 378px;
    width: 100%;
    text-align: center;
    font-size: 45px;
    line-height: 1;
    color: var(--curtain-red);
  }
  .phone {
    position: absolute;
    left: 0;
    top: 460px;
    width: 100%;
    text-align: center;
    font-size: 27px;
    line-height: 1;
  }
  .contact-row {
    position: absolute;
    left: 0;
    top: 517px;
    width: 100%;
    padding: 0 26px 0 58px;
    display: flex;
    justify-content: space-between;
    align-items: baseline;
    font-size: 24px;
    line-height: 1;
  }
  .email { color: var(--text-white); }
  .website { color: var(--curtain-red); }
</style>
</head>
<body>
  <div class="canvas">
    <section class="card" aria-label="Bright Harbor Theatre Academy business card">
      <div class="brand-band">
        <span class="brand-name">Bright Harbor Theatre Academy</span>
      </div>
      <p class="slogan">Step into the limelight</p>
      <p class="owner">Marla Quintrell</p>
      <p class="phone">Phone Number: 303-555-0147</p>
      <div class="contact-row">
        <span class="email">Email: bhtheatreacademy@mailbox-example.com</span>
        <span class="website">Website: bhtheatre-example.com</span>
      </div>
    </section>
  </div>
</body>
</html>
```